Software Development Consulting Company Needs Business Card Design

We need a new business card design for our consultants at Verdant Systems (verdantsystems.example). We are a small firm that provides high-end software development and methodology consulting to medium to large enterprise IT organizations.

Our logo uses Futura for the font and we would like to stick with navy blue and canary yellow for the logo colors. Attached are normal and reversed versions of our logos in illustrator format.
Updates

Hi Everyone, Thank yo very much for your amazing design ideas. I have created a poll for this project and our employees will be voting on the design they wish to use. We will be making a decision this Wednesday (October 22nd). Thanks again, Marcus Hallward

Industry/Entity Type

Business

```html
<!DOCTYPE html>
<html lang="en">
<head>
<meta charset="utf-8">
<title>Verdant Systems — Business Card</title>
<link rel="stylesheet" href="https://fonts.googleapis.com/css2?family=Jost:wght@500&family=Source+Sans+3:wght@400;700&display=swap">
<style>
  :root {
    --navy: #1f4a70;
    --canary: #f6ea0e;
    --paper: #ffffff;
    --ink-grey: #4a4a4a;
    --backdrop: #e9e9ee;
  }
  * { box-sizing: border-box; margin: 0; padding: 0; }
  html, body { width: 1200px; height: 980px; overflow: hidden; }
  body {
    background: var(--backdrop);
    font-family: "Source Sans 3", "Helvetica Neue", Arial, sans-serif;
    position: relative;
  }
  .card {
    position: absolute;
    left: 215px;
    width: 770px;
    height: 440px;
    background: var(--paper);
    border-radius: 30px;
    overflow: hidden;
    box-shadow: 0 10px 28px rgba(0,0,0,0.16);
  }
  .card--back { top: 40px; }
  .card--front { top: 510px; }

  /* Back side */
  .back-brand {
    position: absolute;
    top: 150px;
    left: 0; right: 0;
    display: flex;
    align-items: center;
    justify-content: center;
    gap: 22px;
  }
  .brand-dot {
    width: 34px; height: 34px;
    border-radius: 50%;
    background: var(--canary);
    flex: none;
  }
  .brand-name {
    font-family: "Jost", "Futura", sans-serif;
    font-weight: 500;
    color: var(--navy);
    letter-spacing: 0.08em;
    text-transform: uppercase;
    white-space: nowrap;
  }
  .back-brand .brand-name { font-size: 56px; }
  .back-url {
    position: absolute;
    top: 260px;
    left: 0; right: 0;
    text-align: center;
    font-size: 26px;
    letter-spacing: 0.16em;
    color: var(--ink-grey);
  }

  /* Front side */
  .swoosh {
    position: absolute;
    left: 0; top: 0;
    width: 770px; height: 440px;
  }
  .front-brand {
    position: absolute;
    top: 48px;
    left: 48px;
    display: flex;
    align-items: center;
    gap: 16px;
  }
  .front-brand .brand-dot { width: 22px; height: 22px; }
  .front-brand .brand-name { font-size: 36px; }
  .holder {
    position: absolute;
    top: 128px;
    left: 56px;
  }
  .holder-name {
    font-size: 30px;
    font-weight: 700;
    color: var(--navy);
    line-height: 1.1;
  }
  .holder-title {
    font-size: 20px;
    color: var(--ink-grey);
  }
  .contacts {
    position: absolute;
    right: 48px;
    bottom: 34px;
    color: var(--paper);
    font-size: 20px;
    line-height: 1.5;
    list-style: none;
  }
  .contacts li {
    display: flex;
    align-items: center;
    justify-content: flex-end;
    gap: 10px;
  }
  .contacts svg { width: 18px; height: 18px; flex: none; }
</style>
</head>
<body>

<section class="card card--back" aria-label="Card back">
  <div class="back-brand">
    <span class="brand-dot"></span>
    <span class="brand-name">Verdant Systems</span>
  </div>
  <p class="back-url">www.verdantsystems.example</p>
</section>

<section class="card card--front" aria-label="Card front">
  <svg class="swoosh" viewBox="0 0 770 440" aria-hidden="true">
    <path d="M0 318 C 150 360 260 350 330 290 C 240 335 130 350 0 352 Z" fill="var(--canary)"/>
    <path d="M0 370 C 250 380 420 250 770 40 L770 440 L0 440 Z" fill="var(--navy)"/>
  </svg>

  <div class="front-brand">
    <span class="brand-dot"></span>
    <span class="brand-name">Verdant Systems</span>
  </div>

  <div class="holder">
    <p class="holder-name">Your Name</p>
    <p class="holder-title">Title</p>
  </div>

  <ul class="contacts">
    <li class="contact-phone">
      <svg viewBox="0 0 24 24"><circle cx="12" cy="12" r="10.5" fill="none" stroke="currentColor" stroke-width="2"/><path d="M9 6.5l2 3-1.3 1.2c.6 1.4 1.6 2.4 3 3l1.2-1.3 3 2-1 2.1c-4.5-.2-8.2-3.9-8.4-8.4z" fill="currentColor"/></svg>
      012-555-0142
    </li>
    <li class="contact-email">
      <svg viewBox="0 0 24 24"><rect x="2" y="5" width="20" height="14" rx="2" fill="currentColor"/><path d="M3 6l9 7 9-7" fill="none" stroke="var(--navy)" stroke-width="2"/></svg>
      info@verdantsystems.example
    </li>
    <li class="contact-web">
      <svg viewBox="0 0 24 24" fill="none" stroke="currentColor" stroke-width="1.8"><circle cx="12" cy="12" r="10"/><ellipse cx="12" cy="12" rx="4.5" ry="10"/><path d="M2 12h20M4 7h16M4 17h16"/></svg>
      www.verdantsystems.example
    </li>
    <li class="contact-address">
      <svg viewBox="0 0 24 24"><path d="M12 2a7 7 0 0 0-7 7c0 5 7 13 7 13s7-8 7-13a7 7 0 0 0-7-7z" fill="currentColor"/><circle cx="12" cy="9" r="2.6" fill="var(--navy)"/></svg>
      Lakeport + Ashford, IL
    </li>
  </ul>
</section>

</body>
</html>
```